Bold Creative Business Card for Digital Marketing Company (Contest)

NOTICE TO DESIGNERS: We understand this is how you make your living. Our commitment to you is to give you awesome and rapid feedback. If we don't think you are on the right track or have a chance of winning we will let you know right away so you don't have to focus your time with us and can continue to get work.

We respect the crowdsource community greatly. We have launched hundreds of crowdsource projects and will make this a great experience for you if you choose to participate (we hope you will!)

--------------
Brief
-------------

We are a cutting edge digital marketing company and we need a new, bold and creative business card designed to reflect who we are and what we do. We want our brand to stand out and be noticed.

The name of our company is: Tanglewood Web Marketing

Definition of Tanglewood:

a. a person pursuing rebellious, even potentially disruptive, policies or ideas:

b. a lone dissenter, as an intellectual, an artist, or a politician, who takes an independent stand apart from his or her associates

c. unorthodox, unconventional, nonconformist

Our businesses is helping small to medium size businesses with their online marketing using bold and creative outside the box strategies that get results.

We are an industry leader and need our business cards to stand out when we hand them out to people, and to be amazing so we stand out and "lead the pack"!

Our current website: http://www.tanglewoodwebmarketing.example

We are rebranding our site to reflect the new logo we just got but you will at least have an idea of who we are and what we do.

Colors We Want: We would like to see burnt Orange, Dark Blue, Gray and/or Black.

We need a front and back designed!

Be creative! Even to the point of creative-shaped business cards. Think outside the box. Let nothing stop your imagination! At the very least, we know that we want business cards that are not the US Standard 2"x3.5"... but rather the wider 3.35"x2.17" (European Standard) with rounded corners if you want to stick with a rectangular shape.

On the front we need:

Our Logo
Place for a name ie Paul Dravecki
Place for our phone number (612) 555 - 8806
Place for email name@tanglewoodwebmarketing.example
Place for our website www.TanglewoodWebMarketing.example

Optional... Place for a headshot photo of the person who the business card will be used for

On the back we need:

The wording... FREE VIDEO SERIES! "12 Smart Ideas To Improve Your Business Today!" www.TanglewoodWebMarketing.example/SmartIdeas

We are excited to see what you come up with.

Thank you for your interests and for participating in this contest!
Updates

Hi everyone! Thanks for all your submissions. However, we feel that most of you are "missing" what we're looking for. Almost all of the designs that have come in are what we would call "standard", "generic", or "typical". We are looking for something creative, different, attention-getting, a business card that would stand out amongst a stack of other business cards. I've shot this video: http://clipviewer.example/t/qWpZtRbHmsd Please take the time to review it. Let us know if you have questions. Thanks!

Target Market(s)

Our target market is small to medium sized business owners who need help with their online marketing.

Industry/Entity Type

Marketing

Font styles to use
Sans Serif

Colors
0355a3
85acd3
f78f20
f37022
faa54b
f68d4d

Requirements
Must have
• On the front we need:

Our Logo

Be CREATIVE! INTERESTING!

On the back we need:

Use the colors from our logo!
Nice to have
• Optional... Place for a headshot photo of the person who the business card will be used for.
Should not have
• Boring, "traditional" look and feel. We want and need to stand out!

```html
<!DOCTYPE html>
<html lang="en">
<head>
<meta charset="utf-8">
<title>Tanglewood Web Marketing – Business Card</title>
<link rel="stylesheet" href="https://fonts.googleapis.com/css2?family=Lato:wght@400;700;900&display=swap">
<style>
  :root {
    --backdrop: #d9d9d9;
    --card: #ffffff;
    --ink: #111111;
    --brand-blue: #0355a3;
    --brand-orange: #f37022;
    --accent-orange: #f78f20;
    --photo-frame: #9a9a90;
    --photo-fill-top: #7fa6cf;
    --photo-fill-bottom: #c9b9a6;
  }
  * { margin: 0; padding: 0; box-sizing: border-box; }
  html, body {
    width: 1200px; height: 900px; overflow: hidden;
    background: var(--backdrop);
    font-family: "Lato", Arial, sans-serif;
    color: var(--ink);
  }
  .stage { position: relative; width: 1200px; height: 900px; }

  .card {
    position: absolute;
    width: 520px; height: 337px;
    background: var(--card);
    border-radius: 22px;
    box-shadow: 0 6px 18px rgba(0,0,0,0.18);
  }
  .card--front { left: 90px; top: 80px; }
  .card--back  { left: 590px; top: 480px; }

  /* brand wordmark: one plain square in the logo blue, name in ink */
  .brand { display: flex; align-items: center; gap: 10px; }
  .brand__mark { width: 20px; height: 20px; background: var(--brand-blue); flex: none; }
  .brand__name { font-weight: 900; color: var(--ink); letter-spacing: 0.5px; line-height: 1; white-space: nowrap; }

  .card--front .brand { position: absolute; left: 30px; top: 40px; }
  .card--front .brand__name { font-size: 19px; }

  .headshot {
    position: absolute; right: 26px; top: 26px;
    width: 96px; height: 76px;
    border: 4px solid var(--photo-frame);
    background: linear-gradient(180deg, var(--photo-fill-top), var(--photo-fill-bottom));
  }
  .person {
    position: absolute; right: 128px; top: 74px;
    text-align: right;
  }
  .person__name { font-size: 21px; font-weight: 700; line-height: 1.1; white-space: nowrap; }
  .person__role { font-size: 15px; font-weight: 700; margin-top: 1px; }

  .contact {
    position: absolute; left: 28px; bottom: 24px;
    list-style: none;
  }
  .contact__item {
    display: flex; align-items: center; gap: 8px;
    font-size: 21px; font-weight: 700; line-height: 29px;
    white-space: nowrap;
  }
  .contact__icon { width: 17px; height: 17px; flex: none; }

  .card--back .back-content {
    position: absolute; left: 0; right: 0; top: 100px;
    display: flex; flex-direction: column; align-items: center;
  }
  .card--back .brand { gap: 14px; }
  .card--back .brand__mark { width: 34px; height: 34px; }
  .card--back .brand__name { font-size: 40px; }
  .tagline {
    margin-top: 20px;
    font-size: 19px; color: var(--brand-orange); font-weight: 400;
    white-space: nowrap;
  }
  .offer-url { margin-top: 4px; font-size: 16px; color: var(--ink); white-space: nowrap; }
</style>
</head>
<body>
<main class="stage">

  <section class="card card--front" aria-label="Business card front">
    <div class="brand">
      <span class="brand__mark"></span>
      <span class="brand__name">Tanglewood Web Marketing</span>
    </div>

    <div class="headshot" role="img" aria-label="Headshot photo of the card holder"></div>
    <div class="person">
      <p class="person__name">Paul Dravecki</p>
      <p class="person__role">Director</p>
    </div>

    <ul class="contact">
      <li class="contact__item">
        <svg class="contact__icon" viewBox="0 0 16 16" aria-hidden="true">
          <path fill="var(--brand-orange)" d="M2 5c0-2 2-3 6-3s6 1 6 3v1h-3V5H5v1H2z M4 7h8l2 6H2z"/>
          <circle cx="8" cy="10" r="1.6" fill="#fff"/>
        </svg>
        <span>(612) 555 - 8806</span>
      </li>
      <li class="contact__item">
        <svg class="contact__icon" viewBox="0 0 16 16" aria-hidden="true">
          <rect x="1" y="3" width="14" height="10" fill="var(--brand-orange)"/>
          <path d="M1.5 3.5 8 9l6.5-5.5" fill="none" stroke="#fff" stroke-width="1.3"/>
        </svg>
        <span>@tanglewoodwebmarketing.example</span>
      </li>
      <li class="contact__item">
        <svg class="contact__icon" viewBox="0 0 16 16" aria-hidden="true">
          <circle cx="8" cy="8" r="7" fill="var(--brand-orange)"/>
          <g fill="none" stroke="#fff" stroke-width="1">
            <ellipse cx="8" cy="8" rx="3" ry="7"/>
            <path d="M1 8h14M2.5 4.5h11M2.5 11.5h11"/>
          </g>
        </svg>
        <span>www.TanglewoodWebMarketing.example</span>
      </li>
    </ul>
  </section>

  <section class="card card--back" aria-label="Business card back">
    <div class="back-content">
      <div class="brand">
        <span class="brand__mark"></span>
        <span class="brand__name">Tanglewood</span>
      </div>
      <p class="tagline">"12 Smart Ideas To Improve Your Business Today!"</p>
      <p class="offer-url">www.TanglewoodWebMarketing.example/SmartIdeas</p>
    </div>
  </section>

</main>
</body>
</html>
```